Steady Harbour Coaching Business Card

We need a business card for a new business based in Sydney Australia called "Steady Harbour Coaching". The business provides the following:
1. Resilience systems for individuals - Developing personalised resilience programs that increase stress tolerance, improve work effectiveness and minimise stress responses to challenge.
2. Group Resilience Training for Leaders and managers - Delivering Resilience training packages and ongoing support to leadership cadres within organisations.
3. High Risk Resilience Training - providing resilience training for High Risk professions such as emergency responders, military and police.

Target Market(s)

Corporate / Military / Emergency Responders

Industry/Entity Type

Leadership

Contact Information for Business Card

Steady Harbour Coaching, Derek Falwood, 7/19 Kestrel St Penbrook 2093, quiet.morning.tide@mailpost.example, www.steadyharbourcoaching.example.au, M# 0417603842
Personalised Mental Resilience Systems for leaders and high risk professions

Requirements
Must have
• 1. Creation of a logo/graphic - to include 3 elements:
a. Military
b.Corporate
c. Emergency Responder.

As long as those 3 elements are included - I am open to any potential designs. Preference given to those who can create a logo out of the above three elements.

```html
<!DOCTYPE html>
<html lang="en">
<head>
<meta charset="utf-8">
<title>Steady Harbour Coaching – Business Card</title>
<link href="https://fonts.googleapis.com/css2?family=Open+Sans:wght@400;600;700&display=swap" rel="stylesheet">
<style>
  :root {
    --backdrop: #e9e7e4;
    --card: #ffffff;
    --ink: #3a3a3a;
    --ink-soft: #6d6d6d;
    --band: #f2a81c;
    --band-stripe: #e89a10;
    --band-ink: #2b2418;
    --figure-tone: #3b3b3b;
  }
  * { box-sizing: border-box; margin: 0; padding: 0; }
  html, body {
    width: 1200px; height: 800px; overflow: hidden;
    background: var(--backdrop);
    font-family: "Open Sans", Arial, sans-serif;
  }
  .card {
    position: absolute; left: 100px; top: 110px;
    width: 1000px; height: 580px;
    background: var(--card);
    box-shadow: 0 14px 36px rgba(0,0,0,.18);
    overflow: hidden;
  }
  .card__title {
    position: absolute; right: 40px; top: 38px;
    font-size: 52px; font-weight: 700; letter-spacing: 1px;
    color: var(--ink); text-transform: uppercase; white-space: nowrap;
  }
  .card__figures {
    position: absolute; left: 90px; top: 120px;
    width: 420px; height: 328px;
    border-radius: 6px 6px 0 0;
    background: linear-gradient(180deg, #5a5a5a 0%, var(--figure-tone) 100%);
  }
  .card__band {
    position: absolute; left: 0; right: 0; top: 448px; height: 72px;
    background: repeating-linear-gradient(135deg, var(--band) 0 6px, var(--band-stripe) 6px 9px);
    display: flex; align-items: center; padding: 0 30px 0 34px;
  }
  .card__tagline {
    font-size: 20px; font-weight: 700; color: var(--band-ink);
    text-transform: uppercase; letter-spacing: 0; white-space: nowrap;
  }
  .contact {
    position: absolute; left: 548px; top: 168px;
    color: var(--ink);
  }
  .contact__name {
    font-size: 34px; font-weight: 700; text-transform: uppercase;
    letter-spacing: .5px; line-height: 1.1;
  }
  .contact__email { font-size: 19px; color: var(--ink-soft); margin-top: 2px; }
  .contact__address { font-size: 17px; margin-top: 14px; line-height: 1.25; }
  .contact__address strong { font-weight: 700; }
  .contact__rows { margin-top: 16px; font-size: 17px; line-height: 1.35; }
  .contact__row { display: flex; gap: 14px; }
  .contact__label { font-weight: 700; width: 54px; text-transform: uppercase; }
  .contact__value { color: var(--ink-soft); }
</style>
</head>
<body>
  <div class="card">
    <h1 class="card__title">Steady Harbour Coaching</h1>
    <div class="card__figures" role="img" aria-label="Dark silhouettes of a soldier, a business person and a firefighter standing side by side"></div>
    <div class="card__band">
      <p class="card__tagline">Personalised mental resilience systems for leaders and high risk professions</p>
    </div>
    <div class="contact">
      <p class="contact__name">Derek Falwood</p>
      <p class="contact__email">quiet.morning.tide@mailpost.example</p>
      <p class="contact__address"><strong>7/19</strong> Kestrel<br>St Penbrook 2093</p>
      <div class="contact__rows">
        <div class="contact__row"><span class="contact__label">Call</span><span class="contact__value">0417603842</span></div>
        <div class="contact__row"><span class="contact__label">Web</span><span class="contact__value">www.steadyharbourcoaching.example.au</span></div>
      </div>
    </div>
  </div>
</body>
</html>
```